Product Page

We're marketing an on line educational product, and need a savvy designer to fix a web page that lacks pazazz. We're looking for a designer who can take a lot of information and present it neatly and elegantly, and put all the relevant testimonials in there without loosing cool factor. Right now we need just one page designed, but the winner will have the chance to re-do the entire site, with lots more content coming down the line that will need the new look.

The current page is here: www.kelmartune.com/sign-up. This should be combined with the attached PDF that has a lot more text information.

Note: The previous file listed as a pdf was a jpg. Sorry about that! Now there's a real pdf available for you to download.

I have added a jpg of myself. If you can use that I would appreciate it. I've also uploaded an example of a pricing page. Let me know how you would charge for this extra page.

Target Market(s)

Men and women in their forties who want to improve their singing but have other careers and are looking for high quality voice instruction.

The page must have an attractive "Get Started" button prominently displayed.

Industry/Entity Type

Marketing

Requirements
Must have
• Above the fold: clear buy now button, some testimonials, and the video. Should have a background that makes reading the text easy-not black. The new page must work somehow with the existing theme, although we will be re-designing the whole site soon with your help.
Nice to have
• Some navigation to organize a lot of text

```html
<!DOCTYPE html>
<html lang="en">
<head>
<meta charset="utf-8">
<title>Kelmar Tune School of Voice – Voice Ascent</title>
<link rel="stylesheet" href="https://fonts.googleapis.com/css2?family=Oswald:wght@300;400;500&display=swap">
<style>
:root{
  --blue:#29a9e1;
  --blue-dark:#1a8cc4;
  --ink:#2a2a2a;
  --grey-text:#555;
  --black:#000;
  --white:#fff;
  --logo-dark:#2b2b2b;
}
*{box-sizing:border-box;margin:0;padding:0}
html,body{width:1200px;height:1200px;overflow:hidden;background:var(--white)}
body{position:relative;font-family:Arial,Helvetica,sans-serif;color:var(--ink)}

.hero{position:absolute;left:0;top:0;width:1200px;height:533px;
  background:linear-gradient(90deg,#d6d6d6 0%,#e8e8e8 45%,#e2e2e2 100%)}
.hero-portrait{position:absolute;left:0;top:0;width:445px;height:533px;
  background:radial-gradient(ellipse at 45% 30%,#8a8a8a 0%,#3a3a3a 40%,#0d0d0d 75%)}
.brand-box{position:absolute;left:332px;top:0;width:265px;height:197px}
.brand-box .brand-top{height:117px;background:var(--blue)}
.brand-box .brand-bottom{height:80px;background:var(--logo-dark);color:var(--white);
  text-align:center;padding-top:12px}
.brand-name{font-family:Oswald,sans-serif;font-weight:400;font-size:31px;line-height:34px}
.brand-tag{font-size:17px;line-height:20px}

.top-nav{position:absolute;right:18px;top:25px;font-size:14.5px;color:#111}
.top-nav span{margin:0 5px}

.hero-headline{position:absolute;left:455px;top:255px;width:735px;
  font-family:Oswald,sans-serif;font-weight:300;font-size:41px;line-height:50px;
  color:#333;text-transform:uppercase;white-space:nowrap;letter-spacing:-0.3px}
.hero-headline strong{color:var(--blue);font-weight:500}

.video{position:absolute;left:46px;top:567px;width:438px;height:286px;background:#111;border:1px solid #333}
.video-frame{height:246px;background:radial-gradient(ellipse at 50% 35%,#6a6a6a 0%,#3d3d3d 55%,#2a2a2a 100%);position:relative}
.video-caption{position:absolute;left:70px;right:70px;top:198px;text-align:center;color:#222;
  background:linear-gradient(90deg,transparent,#e6e6e6 25%,#e6e6e6 75%,transparent);padding:3px 0}
.video-caption .name{font-size:13px}
.video-caption .url{font-size:8px}
.video-controls{height:38px;display:flex;align-items:center;gap:6px;padding:0 6px;background:#1b1b1b;font-size:9px;color:#aaa}
.video-track{flex:1;height:22px;background:#3a3a3a;position:relative}
.video-track::before{content:"";position:absolute;left:38px;top:0;width:10px;height:22px;background:var(--blue)}

.btn-start{position:absolute;left:546px;top:570px;width:261px;height:59px;background:var(--blue);
  border:2px solid var(--blue-dark);outline:1px solid #9fd8f2;outline-offset:-5px;
  font-family:Oswald,sans-serif;font-weight:500;font-size:36px;color:var(--white);
  text-align:center;line-height:55px;text-transform:uppercase}
.discount{position:absolute;left:838px;top:582px;font-family:Oswald,sans-serif;font-weight:300;font-size:26px;color:#333}
.discount em{font-style:normal;color:var(--blue)}

.pitch{position:absolute;left:548px;top:648px;width:630px;font-size:16.4px;line-height:20px;color:var(--grey-text)}
.pitch p{margin-bottom:19px}
.signature{position:absolute;left:545px;top:815px;width:135px;height:41px;
  background:linear-gradient(90deg,#cfeefb,#e9f7fd)}

.divider{position:absolute;left:48px;top:879px;width:1106px;height:1px;background:#555}

.testimonial{position:absolute;top:903px;padding-left:110px}
.testimonial .photo{position:absolute;left:0;top:2px;width:88px;height:88px}
.testimonial .quote{font-size:14.3px;line-height:17px;color:#444;margin-top:6px}
.testimonial .who{font-family:Oswald,sans-serif;font-weight:300;font-size:21px;color:#333;line-height:24px;margin-top:4px}
.testimonial .where{font-size:14px;line-height:16px;color:#444}
.t-one{left:47px;width:505px}
.t-one .photo{background:linear-gradient(135deg,#d9c39a,#5a4a3a)}
.t-two{left:657px;width:495px}
.t-two .photo{background:linear-gradient(135deg,#8e7a5e,#3a342c)}

.footer{position:absolute;left:0;top:1037px;width:1200px;height:163px;background:var(--black)}
.footer-brand{position:absolute;left:50px;top:46px;display:flex;align-items:center;gap:12px;color:var(--white)}
.footer-brand .mark{width:44px;height:44px;background:var(--blue)}
.footer-brand .brand-name{font-size:34px;line-height:36px}
.footer-brand .brand-tag{text-align:center}
.footer-links{position:absolute;left:397px;top:66px;font-size:14.5px;color:var(--blue)}
.footer-links span{margin-right:16px}
.copyright{position:absolute;left:397px;top:95px;font-size:13px;color:#ddd}
.social{position:absolute;top:57px;width:50px;height:50px;border-radius:50%}
.social-one{left:1009px;background:#2aa3ef}
.social-two{left:1072px;background:#3b5a99}
</style>
</head>
<body>

<header class="hero">
  <div class="hero-portrait" role="img" aria-label="Black and white portrait of the vocal coach smiling"></div>
  <div class="brand-box">
    <div class="brand-top"></div>
    <div class="brand-bottom">
      <div class="brand-name">Kelmar Tune</div>
      <div class="brand-tag">School of Voice</div>
    </div>
  </div>
  <nav class="top-nav">Voice Lessons<span>|</span>Blog<span>|</span>What Students Say<span>|</span>The Instructors<span>|</span>Voice Ascent</nav>
  <h1 class="hero-headline">Professional vocal coach, <strong>Evan R. Kelmar</strong><br>has laid the vocal foundation for<br>thousands of singers worldwide, for 20+<br>years.</h1>
</header>

<section class="video">
  <div class="video-frame" role="img" aria-label="Video still of the coach speaking to camera">
    <div class="video-caption">
      <div class="name">Evan Robert Kelmar</div>
      <div class="url">www.kelmartune.com</div>
    </div>
  </div>
  <div class="video-controls">
    <svg width="14" height="14" viewBox="0 0 14 14"><rect x="3" y="2" width="3" height="10" fill="#29a9e1"/><rect x="8" y="2" width="3" height="10" fill="#29a9e1"/></svg>
    <span>00:00</span>
    <div class="video-track"></div>
    <span>04:17</span>
    <svg width="48" height="14" viewBox="0 0 48 14"><path d="M1 5h3l4-3v10l-4-3H1z" fill="#29a9e1"/><g fill="#29a9e1"><rect x="12" y="3" width="2" height="8"/><rect x="16" y="3" width="2" height="8"/><rect x="20" y="3" width="2" height="8"/><rect x="24" y="3" width="2" height="8"/><rect x="28" y="3" width="2" height="8"/><rect x="32" y="3" width="2" height="8"/><rect x="36" y="3" width="2" height="8"/><rect x="40" y="3" width="2" height="8"/></g></svg>
    <svg width="22" height="14" viewBox="0 0 22 14"><rect x="1" y="1" width="20" height="12" rx="4" fill="#29a9e1"/></svg>
  </div>
</section>

<div class="btn-start">Get Started</div>
<div class="discount"><em>30% Discount</em> Use Code: VA414</div>

<div class="pitch">
  <p>I believe in Voice Ascent wholeheartedly, and I want you to be fully satisfied with the program.That’s why I stand behind Voice Ascent with a 100%&nbsp; money-back guarantee.</p>
  <p>I am confident that by making this small investment now, you will learn the keys to achieving having a breakthrough with your voice.</p>
  <p>Subcerely yours,</p>
</div>
<div class="signature" role="img" aria-label="Handwritten signature of Evan Kelmar"></div>

<div class="divider"></div>

<article class="testimonial t-one">
  <div class="photo" role="img" aria-label="Portrait photo of Marla Quinn"></div>
  <p class="quote">I have found through the years that the one method I can count on is Voice Ascent. Evan Kelmar has put together the fool proof method for training a voice that is dependable a and authentic as you grow through your vocal practice.</p>
  <div class="who">Marla Quinn</div>
  <div class="where">San Francisco</div>
</article>

<article class="testimonial t-two">
  <div class="photo" role="img" aria-label="Portrait photo of Owen Fairley"></div>
  <p class="quote">Since starting the program, my singing progress has been described as phenomenal, 400% improvement. My teachers have worked with people such as Dame Helena Marsh, and they are impressed with my voice.</p>
  <div class="who">Owen Fairley</div>
  <div class="where">Australia</div>
</article>

<footer class="footer">
  <div class="footer-brand">
    <div class="mark"></div>
    <div>
      <div class="brand-name">Kelmar Tune</div>
      <div class="brand-tag">School of Voice</div>
    </div>
  </div>
  <nav class="footer-links"><span>Home</span><span>About us</span><span>Support</span><span>ERKMethod</span><span>Privacy Policy</span><span>Terms of use</span><span>Sitemap</span></nav>
  <div class="copyright">© Copyright 2009. KelmarTune.com. All Rights Reserved.</div>
  <div class="social social-one"></div>
  <div class="social social-two"></div>
</footer>

</body>
</html>
```